Team email banner for internal communications

We need a team email banner/header that will be applied to all internal communications from our department to other functions. The graphic should be optimized for Outlook and be landscape in layout. We have 5 different silo within our team and will need so will either need have a blank space to denote each team or have change in colors/graphics to denote each team (see current headers attached to job description). We are looking for a banner that combines our team logo (attached) with our team name, Regional Talent & Coaching Unit. The theme should be L&D and pharmaceutical in nature.

Need extra days to review

The text in the banner should be Regional Talent & Coaching Unit with the team logo (attached).

```html
<!DOCTYPE html>
<html lang="en">
<head>
<meta charset="utf-8">
<title>Regional Talent &amp; Coaching Unit — Team Email Banners</title>
<link href="https://fonts.googleapis.com/css2?family=Montserrat:wght@400;500;600;700&family=Poppins:ital,wght@0,400;0,600;0,700;1,700&display=swap" rel="stylesheet">
<style>
  :root{
    --page:#f9f0ee;
    --ink:#111111;
    --white:#ffffff;
    --mark-red:#e0261b;
    --dash:#5a5a5a;
    --band-black:#000000;

    --hema:#d90f0f;      --hema-deep:#a80a0a;   --hema-photo:#d8b4b4;
    --tumor:#87108f;     --tumor-deep:#5f0b66;  --tumor-photo:#2a2444;
    --lead:#fe4a03;      --lead-deep:#c93a04;   --lead-photo:#1e3550;
    --access:#0a46e6;    --access-deep:#3a6fd8; --access-photo:#24405e;
    --ops:#268c0a;       --ops-deep:#0f5a06;    --ops-photo:#18345e;

    --hema-2:#db2a1f;    --tumor-2:#4f1a58;     --lead-2:#ec6c24;
    --access-2:#4b1fd6;  --ops-2:#218ee6;
    --photo-2a:#6a2a2a;  --photo-2b:#2c3c6a;    --photo-2c:#8a8f99;
    --photo-2d:#c9c6c2;  --photo-2e:#5d5f66;
  }
  *{margin:0;padding:0;box-sizing:border-box}
  html,body{width:1200px;height:1200px;overflow:hidden;background:var(--page)}
  .canvas{position:relative;width:1200px;height:1200px;font-family:"Poppins",sans-serif}
  .column-title{position:absolute;top:286px;width:200px;text-align:center;font-family:"Montserrat",sans-serif;font-weight:500;font-size:15px;letter-spacing:.5px;color:var(--ink)}
  .column-title--one{left:280px}
  .column-title--two{left:740px}
  .banner{position:absolute;width:390px;height:90px;display:block}
  .col-one{left:175px}
  .col-two{left:637px}
  .row-1{top:336px}.row-2{top:453px}.row-3{top:571px}.row-4{top:696px}.row-5{top:818px}

  .team-fill{fill:var(--team)}
  .team-stroke{stroke:var(--team)}
  .shade-fill{fill:var(--deep)}
  .photo{fill:var(--photo)}
  .white{fill:var(--white)}
  .mark-dot{fill:var(--mark-red)}
  .mark-name{font-family:"Poppins",sans-serif;font-weight:700;fill:var(--ink)}
  .title-split{font-family:"Poppins",sans-serif;font-weight:700;font-size:28px;fill:var(--white)}
  .sub-split{font-family:"Poppins",sans-serif;font-weight:400;font-size:14px;letter-spacing:1.2px;fill:var(--white)}
  .silo-band{fill:var(--band-black)}
  .silo-split{font-family:"Poppins",sans-serif;font-weight:700;font-style:italic;font-size:14px;letter-spacing:2px;fill:var(--white)}
  .title-round{font-family:"Montserrat",sans-serif;font-weight:600;font-size:40px;fill:var(--white)}
  .sub-round{font-family:"Montserrat",sans-serif;font-weight:500;font-size:15px;fill:var(--white)}
  .silo-round{font-family:"Poppins",sans-serif;font-weight:600;font-size:22px;fill:var(--white)}

  .hema{--team:var(--hema);--deep:var(--hema-deep);--photo:var(--hema-photo)}
  .tumor{--team:var(--tumor);--deep:var(--tumor-deep);--photo:var(--tumor-photo)}
  .lead{--team:var(--lead);--deep:var(--lead-deep);--photo:var(--lead-photo)}
  .access{--team:var(--access);--deep:var(--access-deep);--photo:var(--access-photo)}
  .ops{--team:var(--ops);--deep:var(--ops-deep);--photo:var(--ops-photo)}
  .hema-2{--team:var(--hema-2);--photo:var(--photo-2a)}
  .tumor-2{--team:var(--tumor-2);--photo:var(--photo-2b)}
  .lead-2{--team:var(--lead-2);--photo:var(--photo-2c)}
  .access-2{--team:var(--access-2);--photo:var(--photo-2d)}
  .ops-2{--team:var(--ops-2);--photo:var(--photo-2e)}
</style>
</head>
<body>
<main class="canvas">
  <h2 class="column-title column-title--one">DESIGN 1</h2>
  <h2 class="column-title column-title--two">DESIGN 2</h2>

  <!-- Design one: split banners -->
  <svg class="banner col-one row-1 hema" viewBox="0 0 628 145">
    <rect class="team-fill" width="628" height="145"/>
    <circle class="shade-fill" cx="230" cy="165" r="112"/>
    <circle class="white" cx="82" cy="26" r="86"/>
    <circle cx="230" cy="40" r="92" fill="none" stroke="#fff" stroke-opacity=".45"/>
    <circle class="photo" cx="230" cy="70" r="76" role="img" aria-label="Photo of blood cells under a microscope"/>
    <circle class="white" cx="628" cy="0" r="64"/><circle class="team-fill" cx="642" cy="-12" r="46"/>
    <circle class="mark-dot" cx="82" cy="34" r="9"/>
    <text class="mark-name" x="82" y="78" font-size="30" text-anchor="middle">RTC</text>
    <text class="title-split" x="362" y="62">Regional</text>
    <text class="sub-split" x="362" y="82">Talent &amp; Coaching Unit</text>
    <rect class="silo-band" x="362" y="91" width="266" height="26"/>
    <text class="silo-split" x="376" y="109">HEMATOLOGY</text>
  </svg>

  <svg class="banner col-one row-2 tumor" viewBox="0 0 628 145">
    <rect class="team-fill" width="628" height="145"/>
    <circle class="shade-fill" cx="230" cy="165" r="112"/>
    <circle class="white" cx="82" cy="26" r="86"/>
    <circle cx="230" cy="40" r="92" fill="none" stroke="#fff" stroke-opacity=".45"/>
    <circle class="photo" cx="230" cy="70" r="76" role="img" aria-label="Illustration of a DNA strand with a tumor cell"/>
    <circle class="white" cx="628" cy="0" r="64"/><circle class="team-fill" cx="642" cy="-12" r="46"/>
    <circle class="mark-dot" cx="82" cy="34" r="9"/>
    <text class="mark-name" x="82" y="78" font-size="30" text-anchor="middle">RTC</text>
    <text class="title-split" x="362" y="62">Regional</text>
    <text class="sub-split" x="362" y="82">Talent &amp; Coaching Unit</text>
    <rect class="silo-band" x="362" y="91" width="266" height="26"/>
    <text class="silo-split" x="376" y="109">SOLID TUMOR</text>
  </svg>

  <svg class="banner col-one row-3 lead" viewBox="0 0 628 145">
    <rect class="team-fill" width="628" height="145"/>
    <circle class="shade-fill" cx="230" cy="165" r="112"/>
    <circle class="white" cx="82" cy="26" r="86"/>
    <circle cx="230" cy="40" r="92" fill="none" stroke="#fff" stroke-opacity=".45"/>
    <circle class="photo" cx="230" cy="70" r="76" role="img" aria-label="Photo of a hand holding glowing team icons"/>
    <circle class="white" cx="628" cy="0" r="64"/><circle class="team-fill" cx="642" cy="-12" r="46"/>
    <circle class="mark-dot" cx="82" cy="34" r="9"/>
    <text class="mark-name" x="82" y="78" font-size="30" text-anchor="middle">RTC</text>
    <text class="title-split" x="362" y="62">Regional</text>
    <text class="sub-split" x="362" y="82">Talent &amp; Coaching Unit</text>
    <rect class="silo-band" x="362" y="91" width="266" height="26"/>
    <text class="silo-split" x="376" y="109">LEADERSHIP DEVELOPMENT</text>
  </svg>

  <svg class="banner col-one row-4 access" viewBox="0 0 628 145">
    <rect class="team-fill" width="628" height="145"/>
    <circle class="shade-fill" cx="230" cy="165" r="112"/>
    <circle class="white" cx="82" cy="26" r="86"/>
    <circle cx="230" cy="40" r="92" fill="none" stroke="#fff" stroke-opacity=".45"/>
    <circle class="photo" cx="230" cy="70" r="76" role="img" aria-label="Photo of hands holding a glowing globe"/>
    <circle class="white" cx="628" cy="0" r="64"/><circle class="team-fill" cx="642" cy="-12" r="46"/>
    <circle class="mark-dot" cx="82" cy="34" r="9"/>
    <text class="mark-name" x="82" y="78" font-size="30" text-anchor="middle">RTC</text>
    <text class="title-split" x="362" y="62">Regional</text>
    <text class="sub-split" x="362" y="82">Talent &amp; Coaching Unit</text>
    <rect class="silo-band" x="362" y="91" width="266" height="26"/>
    <text class="silo-split" x="376" y="109">Market Access</text>
  </svg>

  <svg class="banner col-one row-5 ops" viewBox="0 0 628 145">
    <rect class="team-fill" width="628" height="145"/>
    <circle class="shade-fill" cx="230" cy="165" r="112"/>
    <circle class="white" cx="82" cy="26" r="86"/>
    <circle cx="230" cy="40" r="92" fill="none" stroke="#fff" stroke-opacity=".45"/>
    <circle class="photo" cx="230" cy="70" r="76" role="img" aria-label="Illustration of a glowing connected network"/>
    <circle class="white" cx="628" cy="0" r="64"/><circle class="team-fill" cx="642" cy="-12" r="46"/>
    <circle class="mark-dot" cx="82" cy="34" r="9"/>
    <text class="mark-name" x="82" y="78" font-size="30" text-anchor="middle">RTC</text>
    <text class="title-split" x="362" y="62">Regional</text>
    <text class="sub-split" x="362" y="82">Talent &amp; Coaching Unit</text>
    <rect class="silo-band" x="362" y="91" width="266" height="26"/>
    <text class="silo-split" x="376" y="109">Operations &amp; Capabilities</text>
  </svg>

  <!-- Design two: rounded banners -->
  <svg class="banner col-two row-1 hema-2" viewBox="0 0 628 145">
    <rect class="white" width="628" height="145"/>
    <rect class="team-fill" x="0" y="6" width="410" height="134"/>
    <circle class="white" cx="410" cy="73" r="68"/>
    <circle cx="440" cy="73" r="58" fill="none" stroke="#5a5a5a" stroke-dasharray="3 3"/>
    <circle class="team-stroke" cx="410" cy="73" r="56" fill="none" stroke-width="4"/>
    <circle class="photo" cx="410" cy="73" r="45" role="img" aria-label="Close-up photo of a red blood cell"/>
    <circle class="team-fill" cx="353" cy="73" r="5"/>
    <text class="title-round" x="28" y="52">REGIONAL</text>
    <text class="sub-round" x="32" y="75">Talent &amp; Coaching Unit</text>
    <line x1="238" y1="72" x2="312" y2="72" stroke="#fff" stroke-width="1.2"/>
    <text class="silo-round" x="32" y="112">Hematology</text>
    <circle class="mark-dot" cx="560" cy="48" r="12"/>
    <text class="mark-name" x="560" y="118" font-size="44" text-anchor="middle">RTC</text>
    <rect class="team-fill" x="621" y="6" width="7" height="134" rx="3"/>
  </svg>

  <svg class="banner col-two row-2 tumor-2" viewBox="0 0 628 145">
    <rect class="white" width="628" height="145"/>
    <rect class="team-fill" x="0" y="6" width="410" height="134"/>
    <circle class="white" cx="410" cy="73" r="68"/>
    <circle cx="440" cy="73" r="58" fill="none" stroke="#5a5a5a" stroke-dasharray="3 3"/>
    <circle class="team-stroke" cx="410" cy="73" r="56" fill="none" stroke-width="4"/>
    <circle class="photo" cx="410" cy="73" r="45" role="img" aria-label="Illustration of a tumor cell with connecting fibres"/>
    <circle class="team-fill" cx="353" cy="73" r="5"/>
    <text class="title-round" x="28" y="52">REGIONAL</text>
    <text class="sub-round" x="32" y="75">Talent &amp; Coaching Unit</text>
    <line x1="238" y1="72" x2="312" y2="72" stroke="#fff" stroke-width="1.2"/>
    <text class="silo-round" x="32" y="112">Solid Tumor</text>
    <circle class="mark-dot" cx="560" cy="48" r="12"/>
    <text class="mark-name" x="560" y="118" font-size="44" text-anchor="middle">RTC</text>
    <rect class="team-fill" x="621" y="6" width="7" height="134" rx="3"/>
  </svg>

  <svg class="banner col-two row-3 lead-2" viewBox="0 0 628 145">
    <rect class="white" width="628" height="145"/>
    <rect class="team-fill" x="0" y="6" width="410" height="134"/>
    <circle class="white" cx="410" cy="73" r="68"/>
    <circle cx="440" cy="73" r="58" fill="none" stroke="#5a5a5a" stroke-dasharray="3 3"/>
    <circle class="team-stroke" cx="410" cy="73" r="56" fill="none" stroke-width="4"/>
    <circle class="photo" cx="410" cy="73" r="45" role="img" aria-label="Photo of team members joining hands"/>
    <circle class="team-fill" cx="353" cy="73" r="5"/>
    <text class="title-round" x="28" y="52">REGIONAL</text>
    <text class="sub-round" x="32" y="75">Talent &amp; Coaching Unit</text>
    <line x1="238" y1="72" x2="312" y2="72" stroke="#fff" stroke-width="1.2"/>
    <text class="silo-round" x="32" y="112">Leadership Development</text>
    <circle class="mark-dot" cx="560" cy="48" r="12"/>
    <text class="mark-name" x="560" y="118" font-size="44" text-anchor="middle">RTC</text>
    <rect class="team-fill" x="621" y="6" width="7" height="134" rx="3"/>
  </svg>

  <svg class="banner col-two row-4 access-2" viewBox="0 0 628 145">
    <rect class="white" width="628" height="145"/>
    <rect class="team-fill" x="0" y="6" width="410" height="134"/>
    <circle class="white" cx="410" cy="73" r="68"/>
    <circle cx="440" cy="73" r="58" fill="none" stroke="#5a5a5a" stroke-dasharray="3 3"/>
    <circle class="team-stroke" cx="410" cy="73" r="56" fill="none" stroke-width="4"/>
    <circle class="photo" cx="410" cy="73" r="45" role="img" aria-label="Photo of a laptop showing market charts"/>
    <circle class="team-fill" cx="353" cy="73" r="5"/>
    <text class="title-round" x="28" y="52">REGIONAL</text>
    <text class="sub-round" x="32" y="75">Talent &amp; Coaching Unit</text>
    <line x1="238" y1="72" x2="312" y2="72" stroke="#fff" stroke-width="1.2"/>
    <text class="silo-round" x="32" y="112">Market Access</text>
    <circle class="mark-dot" cx="560" cy="48" r="12"/>
    <text class="mark-name" x="560" y="118" font-size="44" text-anchor="middle">RTC</text>
    <rect class="team-fill" x="621" y="6" width="7" height="134" rx="3"/>
  </svg>

  <svg class="banner col-two row-5 ops-2" viewBox="0 0 628 145">
    <rect class="white" width="628" height="145"/>
    <rect class="team-fill" x="0" y="6" width="410" height="134"/>
    <circle class="white" cx="410" cy="73" r="68"/>
    <circle cx="440" cy="73" r="58" fill="none" stroke="#5a5a5a" stroke-dasharray="3 3"/>
    <circle class="team-stroke" cx="410" cy="73" r="56" fill="none" stroke-width="4"/>
    <circle class="photo" cx="410" cy="73" r="45" role="img" aria-label="Photo of a hand at a keyboard with process gear icons"/>
    <circle class="team-fill" cx="353" cy="73" r="5"/>
    <text class="title-round" x="28" y="52">REGIONAL</text>
    <text class="sub-round" x="32" y="75">Talent &amp; Coaching Unit</text>
    <line x1="238" y1="72" x2="312" y2="72" stroke="#fff" stroke-width="1.2"/>
    <text class="silo-round" x="32" y="112">Operations &amp; Capabilities</text>
    <circle class="mark-dot" cx="560" cy="48" r="12"/>
    <text class="mark-name" x="560" y="118" font-size="44" text-anchor="middle">RTC</text>
    <rect class="team-fill" x="621" y="6" width="7" height="134" rx="3"/>
  </svg>
</main>
</body>
</html>
```